Images and design ideas provided: Postcard size flier

2 sided postcard size flier to hand people on the street.

A FUN tax business needs a postcard size flier to hand people on the street. Not a typical serious, quiet, office so make the image fun!

Exact wording, logo and key images provided. You are free to add other images as you see fit (such as money).

Side 1: Use image of lady looking up (she should be looking at text provided).All spanish and english text provided. Logo in bottom right corner. Address at bottom of card.

Side 2: Image of lady holding money and pointing. Remove money and have her holding a sign/or some other creative way to have her looking at text. All spanish and english text provided. Logo in bottom right corner. Address at bottom of card.

Size: 4" x 6" horizontal or vertical is ok
Each side can be different and image/design does not have to be related.

Target Market(s)

Age 18-35

Industry/Entity Type

Accounting

Font styles to use
Sans Serif

Colors

Designer to choose colors to be used in the design.

Requirements
Must have
• Use text document provided. All text goes on both sides.
• Should be easy to read from a few feet away.
Nice to have
• Bright colors to attract attention of people walking by to grab flier/card. Images of money ok.
Should not have
• No images of calculators or typical accounting tax forms.

```html
<!DOCTYPE html>
<html lang="en">
<head>
<meta charset="utf-8">
<title>Refund Royale – Postcard Flier</title>
<link rel="stylesheet" href="https://fonts.googleapis.com/css2?family=Roboto+Condensed:wght@700&family=Fira+Sans:ital,wght@0,500;0,700;1,800&display=swap">
<style>
  :root{
    --board:#3b3b3d;
    --card-white:#ffffff;
    --red:#e31c3d;
    --red-dark:#c8102e;
    --yellow:#fff200;
    --blue:#2f7bc4;
    --navy:#0b4f8e;
    --charcoal:#333335;
    --ink:#111111;
    --paper-light:#f6f5f3;
    --paper-grey:#d9d7d3;
  }
  *{margin:0;padding:0;box-sizing:border-box}
  html,body{width:863px;height:1200px;overflow:hidden;background:var(--board)}
  .board{position:relative;width:863px;height:1200px}

  .card{position:absolute;left:62px;width:731px;background:var(--card-white);
    box-shadow:0 10px 10px rgba(0,0,0,.45)}
  .card--front{top:92px;height:487px}
  .card--back{top:619px;height:488px;
    background:radial-gradient(ellipse at 60% 40%,var(--paper-light) 0%,#ecebe8 55%,var(--paper-grey) 100%)}

  /* front side */
  .front-panel{position:absolute;left:14px;top:14px;width:703px;height:459px;overflow:hidden}
  .front-photo{position:absolute;inset:0;
    background:radial-gradient(ellipse at 75% 40%,#f1f0ee 0%,#dcdad6 70%,#cfccc7 100%)}
  .front-shapes{position:absolute;inset:0}
  .front-figure{position:absolute;left:366px;top:105px;width:270px;height:354px;
    background:linear-gradient(180deg,#d9b24a 0%,#b58b4f 30%,#8f8a5c 60%,#7b7a55 100%);
    border-radius:120px 120px 0 0;opacity:.85}
  .headline{position:absolute;left:26px;font-family:"Roboto Condensed",sans-serif;font-weight:700;
    color:#fff;text-shadow:2px 3px 4px rgba(0,0,0,.35);line-height:1;white-space:nowrap}
  .headline--amount{top:24px;font-size:104px;letter-spacing:-1px}
  .headline--cash{top:124px;font-size:70px;letter-spacing:-1px}
  .offer-note{position:absolute;left:26px;top:222px;font-family:"Fira Sans",sans-serif;font-style:italic;
    font-weight:800;font-size:45px;line-height:54px;color:var(--yellow);
    text-shadow:2px 2px 3px rgba(0,0,0,.35);white-space:nowrap}
  .brand{position:absolute;display:flex;align-items:center;gap:12px;
    font-family:"Fira Sans",sans-serif;font-weight:700;text-transform:uppercase;line-height:1.05;white-space:nowrap}
  .brand__dot{width:22px;height:22px;border-radius:50%;background:var(--blue);flex:none}
  .brand--front{left:26px;top:380px;font-size:28px;color:#fff}

  /* back side */
  .back-photo{position:absolute;left:17px;top:13px;width:390px;height:372px;border-radius:40% 40% 20% 20%;
    background:radial-gradient(ellipse at 50% 35%,#6f8f4a 0%,#8fa27a 40%,#cfd3c6 75%,rgba(230,230,226,0) 100%)}
  .promo{position:absolute;right:40px;top:20px;text-align:right;font-family:"Fira Sans",sans-serif;
    font-style:italic;font-weight:800;font-size:58px;line-height:63px;color:var(--red);letter-spacing:-1px;
    text-shadow:3px 3px 0 var(--charcoal);white-space:nowrap}
  .promo-note{position:absolute;right:40px;top:230px;text-align:right;font-family:"Fira Sans",sans-serif;
    font-weight:500;font-size:28px;line-height:37px;color:var(--ink);white-space:nowrap}
  .address{position:absolute;right:40px;top:375px;font-family:"Fira Sans",sans-serif;font-weight:500;
    font-size:19px;color:var(--navy);white-space:nowrap}
  .phone-band{position:absolute;left:0;top:0;width:731px;height:488px;pointer-events:none}
  .phone{position:absolute;left:460px;top:423px;font-family:"Roboto Condensed",sans-serif;font-weight:700;
    font-size:40px;color:#fff;text-shadow:2px 2px 3px rgba(0,0,0,.35);white-space:nowrap}
  .brand--back{left:24px;top:418px;font-size:28px;color:var(--red)}
</style>
</head>
<body>
<main class="board">

  <section class="card card--front" aria-label="Postcard front, English">
    <div class="front-panel">
      <div class="front-photo" role="img" aria-label="Photo of a cheerful woman in a royal costume and crown pointing at a fan of cash"></div>
      <svg class="front-shapes" viewBox="0 0 703 459" width="703" height="459" aria-hidden="true">
        <path d="M0 0 H500 C438 70 408 170 404 459 H0 Z" fill="var(--red)"/>
        <path d="M500 0 C438 70 408 170 404 459" fill="none" stroke="var(--blue)" stroke-width="9"/>
        <path d="M522 0 C456 72 424 172 418 459" fill="none" stroke="var(--charcoal)" stroke-width="14"/>
      </svg>
      <div class="front-figure" role="img" aria-label="Woman in gold robe holding dollar bills"></div>
      <h1 class="headline headline--amount">GET $100</h1>
      <p class="headline headline--cash">Cash Now!</p>
      <p class="offer-note">With Paid Tax<br>Preparation</p>
      <div class="brand brand--front"><span class="brand__dot"></span><span>Refund<br>Royale</span></div>
    </div>
  </section>

  <section class="card card--back" aria-label="Postcard back, Spanish">
    <div class="back-photo" role="img" aria-label="Photo of a bonsai money tree with dollar bills hanging from its branches and scattered around the pot"></div>
    <h2 class="promo">Reciba $100<br>en efectivo<br>ahora!</h2>
    <p class="promo-note">con la preparacion<br>pagada de sus<br>impuestos</p>
    <p class="address">415 Marlow Ave. Bronx NY 10460</p>
    <svg class="phone-band" viewBox="0 0 731 488" width="731" height="488" aria-hidden="true">
      <polygon points="444,414 731,414 731,488 410,488" fill="var(--navy)"/>
    </svg>
    <p class="phone">(718) 555-0147</p>
    <div class="brand brand--back"><span class="brand__dot"></span><span>Refund<br>Royale</span></div>
  </section>

</main>
</body>
</html>
```